Poster Needed for Church Conference

I need a poster for a weekend conference at my church. Looking to attract as many people as possible. We are a church in the suburbs of Houston. This is mainly for our own church members but we are opening it up to outside church members.

Please see previous design from last conference and all other graphic work that can (doesn't need to be) included.

Target Market(s)

It's targeted for all people. But our main audience is families. around the age of 30 should be main target.

Industry/Entity Type

Non-Profit

Font styles to use
Serif
Sans Serif

Colors

Designer to choose colors to be used in the design.

Requirements
Must have
• 11x17 design with ability to shrink and blow up. but ideally for 11x17
• Content and wording:
• "Rooted Lantern Conference: Bridging the gap between generations and passing on our deepest beliefs and values."
• Featuring Dr. Glen Marlowe. Author of "The Map of Q9"
• Aug 25-26: Friday 8-10 pm, Saturday 4-8 pm
• Cost Adults $15/Children $5: Covers admission to all sessions and workshops, refreshments and Saturday dinner. *kids 5 and under free
• Childcare provided for all sessions. "
• Please use church logo and address on flyer: 4312 Orchard Bend, Larkfield City, LF 77512
Nice to have
• Ideally it will be designed so that we can crop a 16:9 pp announcement slide and header for our website.
Should not have
• anything offensive

```html
<!DOCTYPE html>
<html lang="en">
<head>
<meta charset="utf-8">
<title>Rooted Lantern Conference</title>
<link rel="stylesheet" href="https://fonts.googleapis.com/css2?family=Cinzel:wght@400;700&family=Almendra&family=Montserrat:wght@600;800&family=Roboto+Condensed:wght@700&display=swap">
<style>
  :root {
    --bg-dark: #262626;
    --edge-green: #3f9a2c;
    --church-green: #3fae52;
    --bright-green: #46ee1e;
    --text-light: #e6e6e6;
    --text-muted: #c4c4c4;
    --white: #ffffff;
  }
  * { margin: 0; padding: 0; box-sizing: border-box; }
  html, body { width: 1200px; height: 676px; overflow: hidden; background: var(--bg-dark); }
  .poster { position: relative; width: 1200px; height: 676px; overflow: hidden; font-family: "Cinzel", serif; }
  .backdrop { position: absolute; inset: 0; }
  .church-name {
    position: absolute; top: 12px; left: 0; width: 1200px; text-align: center;
    font-size: 30px; font-variant: small-caps; color: var(--church-green); letter-spacing: 1px;
  }
  .event-title {
    position: absolute; top: 58px; left: 0; width: 1200px; text-align: center;
    font-family: "Montserrat", sans-serif; font-weight: 800; font-size: 52px;
    color: var(--bright-green); letter-spacing: -1.5px;
  }
  .tagline {
    position: absolute; top: 128px; left: 185px; width: 830px; text-align: center;
    font-weight: 700; font-size: 22px; line-height: 29px; font-variant: small-caps;
    color: var(--text-light);
  }
  .speaker-photo {
    position: absolute; left: 172px; top: 223px; width: 187px; height: 187px;
    border-radius: 32px; background: radial-gradient(circle at 55% 40%, #8a6d5c 0%, #3b2d25 45%, #050505 80%);
  }
  .book-cover {
    position: absolute; left: 379px; top: 290px; width: 84px; height: 116px;
    background: linear-gradient(160deg, #ffffff 0%, #e4e4e4 60%, #bdbdbd 100%);
  }
  .speaker {
    position: absolute; top: 420px; left: 170px; width: 330px; text-align: center;
    font-family: "Almendra", serif; font-size: 25px; line-height: 36px; color: var(--text-light);
  }
  .book-title { font-family: "Roboto Condensed", sans-serif; font-weight: 700; color: var(--white); }
  .event-date {
    position: absolute; left: 693px; top: 226px; font-size: 38px; font-weight: 700;
    color: var(--white);
  }
  .event-date sup { font-size: 20px; vertical-align: 16px; }
  .details { position: absolute; left: 714px; top: 282px; width: 380px; }
  .detail-row { position: relative; }
  .detail-label {
    position: absolute; left: 0; font-family: "Almendra", serif; font-size: 20px; color: var(--text-muted);
  }
  .detail-value {
    margin-left: 86px; font-weight: 700; font-variant: small-caps; font-size: 21px;
    color: var(--bright-green); line-height: 29px;
  }
  .row-cost { margin-top: 3px; }
  .row-cost .detail-value { line-height: 23px; }
  .cost-note {
    font-size: 14px; font-variant: small-caps; color: var(--text-muted); line-height: 15px; margin-top: 3px;
    white-space: nowrap;
  }
  .row-venue { margin-top: 16px; }
  .row-venue .detail-value { width: 190px; text-align: center; line-height: 24px; }
  .footnote {
    position: absolute; top: 644px; font-family: "Montserrat", sans-serif; font-weight: 600;
    font-size: 15px; color: var(--text-muted);
  }
  .footnote-kids { left: 67px; }
  .footnote-childcare { left: 314px; }
  .church-mark {
    position: absolute; left: 1000px; top: 634px; display: flex; align-items: center; gap: 8px;
    font-family: "Cinzel", serif; font-weight: 700; font-size: 14px; color: var(--text-light);
  }
  .church-mark-square { width: 14px; height: 14px; background: var(--text-light); }
</style>
</head>
<body>
<div class="poster">
  <svg class="backdrop" width="1200" height="676" viewBox="0 0 1200 676" aria-hidden="true">
    <defs>
      <linearGradient id="panelShade" x1="0" y1="0" x2="1" y2="1">
        <stop offset="0" stop-color="#4d4d4d"/>
        <stop offset="1" stop-color="#444444"/>
      </linearGradient>
      <linearGradient id="sideShade" x1="0" y1="0" x2="1" y2="0">
        <stop offset="0" stop-color="#1c1c1c"/>
        <stop offset="1" stop-color="#353535"/>
      </linearGradient>
    </defs>
    <rect width="1200" height="676" fill="url(#sideShade)"/>
    <polygon points="156,0 1192,0 1088,676 -10,676 -10,600" fill="url(#panelShade)"/>
    <line x1="156" y1="0" x2="-6" y2="614" stroke="var(--edge-green)" stroke-width="1.2"/>
    <line x1="1192" y1="0" x2="1088" y2="676" stroke="var(--edge-green)" stroke-width="1.2"/>
  </svg>

  <div class="church-name">Cedar Hollow Community Church</div>
  <h1 class="event-title">ROOTED LANTERN CONFERENCE</h1>
  <p class="tagline">"Bridging the gap between generations and passing on our deepest beliefs and values."</p>

  <div class="speaker-photo" role="img" aria-label="Portrait photo of the featured speaker"></div>
  <div class="book-cover" role="img" aria-label="Cover of the book The Map of Q9"></div>

  <div class="speaker">
    <div>Featuring</div>
    <div>Dr. Glen Marlowe</div>
    <div>Author of "<span class="book-title">The Map of Q9</span>"</div>
  </div>

  <div class="event-date">AUGUST 25<sup>TH</sup> &amp; 26<sup>TH</sup></div>

  <div class="details">
    <div class="detail-row row-timings">
      <span class="detail-label">Timings</span>
      <div class="detail-value">Friday 8 PM - 10 pm<br>Saturday 4 PM - 8 pm</div>
    </div>
    <div class="detail-row row-cost">
      <span class="detail-label">Cost</span>
      <div class="detail-value">Adults $15/<br>Children $5</div>
      <div class="cost-note">Covers admission to all sessions and workshops,<br>refreshments and Saturday dinner.</div>
    </div>
    <div class="detail-row row-venue">
      <span class="detail-label">Venue</span>
      <div class="detail-value">4312 Orchard Bend<br>Larkfield City<br>LF 77512</div>
    </div>
  </div>

  <div class="footnote footnote-kids">*kids 5 and under free</div>
  <div class="footnote footnote-childcare">Childcare provided for all sessions. "</div>

  <div class="church-mark">
    <span class="church-mark-square"></span>
    <span>Cedar Hollow Church</span>
  </div>
</div>
</body>
</html>
```